Wing House Menu Design Project

Traditional wing house restaurant chain

Specs are: Tri-fold laminated menu

11”h x 17”W folded to 11”h x 5.66”w

Full color

Logos and text supplied

Wants a clean look with text layout as follows:

Cover – Original Logo

Tag line text to go on front cover:

*Through our doors walk the most important people in the world… you, our customers.

*A Family, Fun, Foodery

Inside left panel: appetizer/salads & wrap

Middle panel (highlighted in a way to make this pop): our famous traditional wings, our soon to be famous florpz (hold spot for photo), Combos on bottom middle panel

Inside right panel: burgers (hold spot for picture), sandwiches underneath

Swing panel: desserts, lunch specials

Back panel: 365 flavor profiles and how it started story … proudly serves…. On the bottom to list logos: kettle barn, Voltry, oak tally, lupa fizz, Pelvane foods, Drulo, brake

· Do not put dollar signs

· Do not put price leaders…………. Before pricing

Current menu is http://tomsfeastandhearth.example/wp-content/uploads/2011/09/tomsfeast_menu.pdf

Looking to get a fresh NEW look!

Good Afternoon Everyone!! Please make your changes ASAP so we can make a decision.. I have messaged some of you, please pay attention to the details, this means more than you know.. It's not JUST about concept- i am presenting these to a client who is expecting their correct menu text in the menu design. It's VERY IMPORTANT that this is done. The time spend it creating the word documents of menu item text was for you to use them. Please message me if you have ANY questions at all.. We are looking forward to a perfect design! Thanks to everyone for your hard work thus far!! :)

This is a Wing House, so the middle inside panel needs to POP and make you WANT TO ORDER WINGS!!!

Thanks!

```html
<!DOCTYPE html>
<html lang="en">
<head>
<meta charset="utf-8">
<title>Tom's Feast &amp; Hearth – Inside Menu</title>
<link rel="stylesheet" href="https://fonts.googleapis.com/css2?family=Noto+Sans:wght@400;700&family=Titillium+Web:wght@600;700&display=swap">
<style>
  :root {
    --orange: #e8521f;
    --orange-deep: #d63c22;
    --red-line: #c8302a;
    --ink: #1d1d1d;
    --paper: #ffffff;
    --wing-tint: #fff0e6;
    --photo-a: #c9662b;
    --photo-b: #8a3a1a;
  }
  * { box-sizing: border-box; margin: 0; padding: 0; }
  html, body { width: 1200px; height: 900px; overflow: hidden; background: var(--paper); }
  body { position: relative; font-family: "Noto Sans", Verdana, sans-serif; color: var(--ink); font-size: 8.4px; line-height: 11px; }

  .wing-panel { position: absolute; left: 400px; top: 106px; width: 400px; height: 346px; background: var(--wing-tint); }

  .section-head { position: absolute; width: 400px; height: 95px; }
  .section-head svg { position: absolute; left: 0; top: 0; width: 400px; height: 95px; }
  .section-head h2 {
    position: absolute; left: 12px; top: 5px;
    font-family: "Titillium Web", "Arial Narrow", sans-serif; font-weight: 700;
    font-size: 25px; line-height: 34px; color: var(--paper); letter-spacing: .3px;
  }
  .section-head.caps h2 { font-size: 24px; letter-spacing: .6px; }

  .block { position: absolute; }
  .item { margin-bottom: 8px; }
  .tag {
    display: inline-block; background: var(--orange); color: var(--paper);
    font-weight: 700; font-size: 8px; line-height: 10px; padding: 0 5px;
    border-radius: 6px; margin-bottom: 1px;
  }
  .line { display: flex; align-items: baseline; white-space: nowrap; }
  .line .gap { flex: 1; min-width: 8px; }
  .note { margin-bottom: 8px; }

  .wings-list { font-size: 11.5px; line-height: 13.5px; width: 228px; }

  .photo-spot {
    position: absolute; width: 118px; border-radius: 6px;
    background: linear-gradient(150deg, var(--photo-a), var(--photo-b));
    border: 3px solid var(--paper); box-shadow: 0 0 0 1px var(--red-line);
  }
</style>
</head>
<body>

<div class="wing-panel"></div>

<!-- Section headers -->
<header class="section-head" style="left:0;top:62px">
  <svg viewBox="0 0 400 95" aria-hidden="true"><rect width="400" height="40" fill="var(--orange)"/><rect y="40" width="400" height="4" fill="var(--red-line)"/><circle cx="334" cy="17" r="68" fill="var(--red-line)"/><circle cx="334" cy="17" r="66" fill="var(--paper)"/><circle cx="334" cy="17" r="62" fill="var(--orange)"/></svg>
  <h2>Appetizers</h2>
</header>
<header class="section-head caps" style="left:400px;top:62px">
  <svg viewBox="0 0 400 95" aria-hidden="true"><rect width="400" height="40" fill="var(--orange)"/><rect y="40" width="400" height="4" fill="var(--red-line)"/><circle cx="334" cy="17" r="68" fill="var(--red-line)"/><circle cx="334" cy="17" r="66" fill="var(--paper)"/><circle cx="334" cy="17" r="62" fill="var(--orange)"/></svg>
  <h2>TRADITIONAL WINGS</h2>
</header>
<header class="section-head caps" style="left:800px;top:62px">
  <svg viewBox="0 0 400 95" aria-hidden="true"><rect width="400" height="40" fill="var(--orange)"/><rect y="40" width="400" height="4" fill="var(--red-line)"/><circle cx="334" cy="17" r="68" fill="var(--red-line)"/><circle cx="334" cy="17" r="66" fill="var(--paper)"/><circle cx="334" cy="17" r="62" fill="var(--orange)"/></svg>
  <h2>BURGERS</h2>
</header>
<header class="section-head" style="left:400px;top:270px">
  <svg viewBox="0 0 400 95" aria-hidden="true"><rect width="400" height="40" fill="var(--orange)"/><rect y="40" width="400" height="4" fill="var(--red-line)"/><circle cx="334" cy="17" r="68" fill="var(--red-line)"/><circle cx="334" cy="17" r="66" fill="var(--paper)"/><circle cx="334" cy="17" r="62" fill="var(--orange)"/></svg>
  <h2 style="font-size:19px">Our soon to befamous FLORPZ</h2>
</header>
<header class="section-head" style="left:400px;top:452px">
  <svg viewBox="0 0 400 95" aria-hidden="true"><rect width="400" height="40" fill="var(--orange)"/><rect y="40" width="400" height="4" fill="var(--red-line)"/><circle cx="334" cy="17" r="68" fill="var(--red-line)"/><circle cx="334" cy="17" r="66" fill="var(--paper)"/><circle cx="334" cy="17" r="62" fill="var(--orange)"/></svg>
  <h2>Lunch Combos</h2>
</header>
<header class="section-head caps" style="left:800px;top:452px">
  <svg viewBox="0 0 400 95" aria-hidden="true"><rect width="400" height="40" fill="var(--orange)"/><rect y="40" width="400" height="4" fill="var(--red-line)"/><circle cx="334" cy="17" r="68" fill="var(--red-line)"/><circle cx="334" cy="17" r="66" fill="var(--paper)"/><circle cx="334" cy="17" r="62" fill="var(--orange)"/></svg>
  <h2>SANDWICHES</h2>
</header>
<header class="section-head" style="left:0;top:510px">
  <svg viewBox="0 0 400 95" aria-hidden="true"><rect width="400" height="40" fill="var(--orange)"/><rect y="40" width="400" height="4" fill="var(--red-line)"/><circle cx="334" cy="17" r="68" fill="var(--red-line)"/><circle cx="334" cy="17" r="66" fill="var(--paper)"/><circle cx="334" cy="17" r="62" fill="var(--orange)"/></svg>
  <h2>Salads / Wraps</h2>
</header>

<!-- Appetizers -->
<section class="block" style="left:22px;top:146px;width:172px">
  <div class="item"><span class="tag">Nachos</span>
    <p>Crisp corn tortillas smothered in melted cheese w/ jalapeños, sour cream and salsa on</p>
    <div class="line">the side!<span class="gap"></span>6.99</div>
    <div class="line">Nacho Supreme<span class="gap"></span>8.99</div>
    <p style="margin-top:11px">Chili, cheese, lettuce, tomatoes, onions and jalapeños, sour cream and salsa on the side</p>
    <div class="line">Add Grilled Chicken<span class="gap"></span>9.99</div>
    <div class="line">Add Buffalo Chicken<span class="gap"></span>11.09</div>
  </div>
  <div class="item"><span class="tag">Quesadillas</span>
    <p>Two flour tortillas stuffed w/ Tom's threecheese blend, served w/ sour cream, salsa and</p>
    <div class="line">jalapeños on the side.<span class="gap"></span>5.79</div>
    <div class="line">Add Grilled Chicken<span class="gap"></span>8.29</div>
    <div class="line">Add Buffalo Chicken<span class="gap"></span>8.29</div>
    <div class="line">Add Steak<span class="gap"></span>x.xx</div>
  </div>
  <div class="item"><span class="tag">Mushrooms</span>
    <p>Fresh, juicy, hand battered and served w/ ranch dressing.</p>
    <div class="line">The best in the land!<span class="gap"></span>5.99</div>
  </div>
  <div class="item"><span class="tag">Black &amp; Bleu Fries</span>
    <p>Our famous waffle fries topped w/ chunky bleu cheese dressing, crumbled bacon and seasoned</p>
    <div class="line">with a Cajun spice blend<span class="gap"></span>3.99</div>
  </div>
</section>

<section class="block" style="left:205px;top:144px;width:176px">
  <div class="item"><span class="tag">Mozzarella Stix</span>
    <p>Lightly breaded, cooked crisp and served w/</p>
    <div class="line">our rich marinara sauce<span class="gap"></span>5.29</div>
  </div>
  <div class="item"><span class="tag">Fried Pickles</span>
    <p>Freshly sliced, lightly breaded and fried golden-brown. Served w/ ranch</p>
    <div class="line">dressing<span class="gap"></span>4.29</div>
  </div>
  <div class="item"><span class="tag">Fried Squash</span>
    <p>Fresh from the garden, deep fried, and</p>
    <div class="line">served w/ bleu cheese dressing<span class="gap"></span>4.59</div>
  </div>
  <div class="item"><span class="tag">Onion Rings</span>
    <p>They'll make you scream for more! Thickly sliced onion rings, coated with a beerseasoned batter and served crispy,</p>
    <div class="line">goldenbrown w/ Petal sauce<span class="gap"></span>5.79</div>
  </div>
  <div class="item"><span class="tag">Waffle Fries</span>
    <p>Choose a new cut on an old twist or fries</p>
    <div class="line">exceeding the weight requirement!<span class="gap"></span>2.39</div>
    <div class="line">Add Chili<span class="gap"></span>0.99</div>
    <div class="line">Add Cheese<span class="gap"></span>0.99</div>
    <div class="line">Add Bacon<span class="gap"></span>0.99</div>
    <div class="line">Add Jalapeños<span class="gap"></span>0.99</div>
  </div>
  <div class="item"><span class="tag">House Soup or Soup of the day</span>
    <div class="line">Fake text to hold place<span class="gap"></span>X.xx</div>
  </div>
  <div class="item"><span class="tag">Soft Pretzel</span>
    <div class="line">Fake text to hold place<span class="gap"></span>X.xx</div>
  </div>
</section>

<!-- Wings -->
<section class="block wings-list" style="left:420px;top:148px">
  <div class="line">5 pieces<span class="gap"></span>5.99</div>
  <div class="line">10 pieces<span class="gap"></span>11.19</div>
  <div class="line">20 pieces<span class="gap"></span>17.49</div>
  <div class="line">50 pieces<span class="gap"></span>46.89</div>
</section>
<div class="photo-spot" style="left:668px;top:160px;height:96px" role="img" aria-label="Photo spot: plate of traditional wings"></div>

<section class="block wings-list" style="left:420px;top:337px">
  <div class="line">5 pieces<span class="gap"></span>5.99</div>
  <div class="line">10 pieces<span class="gap"></span>11.19</div>
  <div class="line">20 pieces<span class="gap"></span>17.49</div>
  <div class="line">50 pieces<span class="gap"></span>46.89</div>
</section>
<div class="photo-spot" style="left:668px;top:350px;height:90px" role="img" aria-label="Photo spot: basket of florpz"></div>

<!-- Lunch combos -->
<section class="block" style="left:424px;top:527px;width:234px">
  <p class="note">Lunch Specials M–F, 11–4 p.m.<br>Only combos are served w/ choice of side and 20oz drink.</p>
  <div style="margin-top:15px">
    <div class="line">5-Boneless Wing Combo<span class="gap"></span>5.99</div>
    <div class="line">Lunch Tender Combo<span class="gap"></span>5.29</div>
  </div>
  <span class="tag" style="margin-top:13px">Lunch Portion Salads &amp; Quesadillas</span>
  <div style="margin-top:10px">
    <div class="line">Buffalo Chicken Quesadilla<span class="gap"></span>5.79</div>
    <div class="line">Grilled Chicken Quesadilla<span class="gap"></span>5.29</div>
    <div class="line">Buffalo Chicken Salad<span class="gap"></span>6.79</div>
    <div class="line">Grilled Chicken Salad<span class="gap"></span>6.29</div>
  </div>
</section>

<!-- Salads / Wraps -->
<section class="block" style="left:24px;top:566px;width:190px">
  <p>All salads served w/ choice of French, Ranch, Lite Ranch, Bleu Cheese, Honey Mustard, Thousand Island, Italian or Lite Italian dressing.</p>
</section>
<section class="block" style="left:20px;top:610px;width:196px">
  <div class="item"><span class="tag">Buffalo Tender Salad</span>
    <p>Lightly breaded tenders cut into bite size pieces</p>
    <div class="line">w/ your choice of Tom's 365 varieties<span class="gap"></span>9.49</div>
  </div>
  <div class="item"><span class="tag">Grilled Chicken Salad</span>
    <p>Fresh, marinated chicken, grilled, and served on</p>
    <div class="line">equally fresh greens<span class="gap"></span>8.79</div>
  </div>
  <div class="item"><span class="tag">Steak Salad</span>
    <div class="line">Text to hold place<span class="gap"></span>x.xx</div>
  </div>
  <div class="item"><span class="tag">Tom's House Salad</span>
    <p>Fresh crisp lettuce, tomato, cucumber, onion and cheese topped off w/ our delicious homemade croutons and your favorite dressing</p>
    <div class="line">on the side<span class="gap"></span>3.49</div>
  </div>
  <div class="item"><span class="tag">Small House Salad</span>
    <div class="line">Tex to hold place<span class="gap"></span>x.xx</div>
  </div>
</section>
<section class="block" style="left:226px;top:602px;width:158px">
  <p class="note">All wraps served w/ potato salad</p>
  <div class="item"><span class="tag">Buffalo Wrap</span>
    <p>Chicken tenders shaken in your favorite Tom's sauce, then rolled w/ cucumbers, lettuce, tomatoes</p>
    <div class="line">and our three-cheese mix<span class="gap"></span>7.69</div>
  </div>
  <div class="item"><span class="tag">Grilled Chicken Wrap</span>
    <p>Marinated, grilled chicken, cucumbers, onions, tomatoes and lettuce together w/ our three-cheese mix and Tom's</p>
    <div class="line">Famous Cajun Ranch sauce<span class="gap"></span>7.39</div>
  </div>
  <div class="item"><p>Continued wraps:</p><span class="tag">Philly Steak Wrap</span>
    <div class="line">xxxxxxxxxxxxxxxxxxxx<span class="gap"></span>x.xx</div>
  </div>
  <div class="item"><span class="tag">Fish Taco Wrap</span>
    <div class="line">xxxxxxxxxxxxxxxxxxxxx<span class="gap"></span>x.xx</div>
  </div>
</section>

<!-- Burgers -->
<section class="block" style="left:816px;top:131px;width:268px">
  <p>All burgers are fresh, black Angus steak and served with a side of chips, potato salad, coleslaw, bakes beans or Texas toast. 1.00 up charge for waffle fries or side salad</p>
</section>
<section class="block" style="left:818px;top:186px;width:176px">
  <div class="item"><span class="tag">The Traditional</span>
    <p style="margin-bottom:11px">All you need for the classic favorite: lettuce,</p>
    <div class="line">tomato and onion<span class="gap"></span>7.39</div>
    <div class="line">Add Chili<span class="gap"></span>0.99</div>
    <div class="line">Add Cheese<span class="gap"></span>0.99</div>
    <div class="line">Any 365 Sauce<span class="gap"></span>0.59</div>
  </div>
  <div class="item"><span class="tag">The Squealin' Cheeser</span>
    <p style="margin-bottom:11px">Bacon, Swiss and garden stuff to make you</p>
    <div class="line">proud to eat like a pig!<span class="gap"></span>8.49</div>
  </div>
  <div class="item"><span class="tag">The Three Cheeser</span>
    <p style="margin-bottom:11px">American, Cheddar and Jack melted on top</p>
    <div class="line">of a juicy patty<span class="gap"></span>8.59</div>
  </div>
  <div class="item"><span class="tag">Add Fresh Grilled Onions and Melted</span>
    <div class="line" style="margin-top:11px">Swiss<span class="gap"></span>0.40</div>
  </div>
</section>
<section class="block" style="left:1004px;top:186px;width:174px">
  <div class="item"><span class="tag">The Shroomer</span>
    <p style="margin-bottom:11px">Delicious Swiss dripping over sautéed</p>
    <div class="line">mushrooms. You'll trip over it!<span class="gap"></span>8.49</div>
  </div>
  <div class="item"><span class="tag">Cajun Ranch Burger</span>
    <p style="margin-bottom:11px">Our traditional burger w/ Cajun and ranch</p>
    <div class="line">dressing<span class="gap"></span>8.49</div>
  </div>
  <div class="item"><span class="tag">Patty Melt</span>
    <p style="margin-bottom:11px">You choose the cheese, we choose the sautéed onions and grilled Texas</p>
    <div class="line">Toast<span class="gap"></span>8.39</div>
  </div>
  <div class="item"><span class="tag">Burger Sliders</span>
    <div class="line" style="margin-top:11px">Hold place with text<span class="gap"></span>X.XX</div>
  </div>
</section>

<!-- Sandwiches -->
<section class="block" style="left:812px;top:522px;width:260px">
  <p>All sandwiches come with a side of chips, potato salad, coleslaw, bakes beans or Texas toast. 1.00 up charge for waffle fries or side salad</p>
</section>
<section class="block" style="left:814px;top:579px;width:180px">
  <div class="item"><span class="tag">The Grilled Chicken Classic</span>
    <p>Charbroiled to perfection and served original</p>
    <div class="line">or Cajun spiced<span class="gap"></span>8.39</div>
  </div>
  <div class="item"><span class="tag">Hot Lap Buffalo Chicken Sandwich</span>
    <p>Lightly breaded chicken breast shaken</p>
    <div class="line">w/ any of Tom's 365 varieties<span class="gap"></span>8.59</div>
  </div>
  <div class="item"><span class="tag">Steak or Chicken Philly</span>
    <p>Tender chunks of charbroiled chicken or steak topped w/ sautéed onions, mushrooms, peppers and melted provolone cheese on a freshly toasted</p>
    <div class="line">hoagie roll<span class="gap"></span>8.89</div>
  </div>
</section>
<section class="block" style="left:1001px;top:579px;width:178px">
  <div class="item"><span class="tag">The Grilled Chicken Classic</span>
    <p>Add our Hickory BBQ sauce, bacon and Swiss</p>
    <div class="line">cheese to our classic<span class="gap"></span>8.99</div>
  </div>
  <div class="item"><span class="tag">Hot Dog</span>
    <p>1/4 lb. all-beef dog grilled to perfection, served on a toasted bun. Onions and relish</p>
    <div class="line">available on request<span class="gap"></span>3.95</div>
    <div class="line">Add Chili<span class="gap"></span>0.99</div>
    <div class="line">Add Cheese<span class="gap"></span>0.99</div>
    <div class="line">Add Slaw<span class="gap"></span>0.99</div>
  </div>
  <div class="item"><span class="tag">Catch of the Day Sandwich</span>
    <p>Served w/ chips. Fisherman's catch cooked the way you like it: fried,</p>
    <div class="line">Cajun or broiled<span class="gap"></span>9.59</div>
  </div>
  <div class="item"><span class="tag">Chicken Sliders</span>
    <p>(3)2 oz tenders</p>
    <p>xxxxxxxxxxxxxxxxxxxxxxxxxxxxxx</p>
    <div class="line">xxxxxxxxxxxxxxxxxxxx<span class="gap"></span>x.xx</div>
  </div>
</section>

</body>
</html>
```